Verdane Clinical Spa needs an eye-catching poster to help promote our largest sale of spring!

We need a poster that will go on the back of the doors in the patient rooms. Our medical spa is professional and high-end, so we want the poster to look sophisticated, yet very eye-catching.
This project is for our Marigold Jubilee special, our second largest sale of the year.

Name: Marigold Jubilee
Slogan: Let Your Beauty Bloom
Sale: The More You Buy, The More You Save

Choose from your favorite spa services
NEVRIL, Laser Treatments, Microderms, and More!

It would be great to have something blooming. Flowers, or somehow make a woman look like she's blooming.

I am attaching a visual description of our special. However, the poster should NOT include the pricing tiers. I am also attaching our business logo. Thank you!!

Target Market(s)

A majority are women, but some are men. Around 25-55 in age. Middle to upper class who are likely to spend more money.

Industry/Entity Type

Medical

Font styles to use
Sans Serif
Script

Colors

Designer to choose colors to be used in the design.

Requirements
Must have
• Name of promotion: Marigold Jubilee
• Slogan: "Let Your Beauty Bloom"
• Concept "The more you buy, the more you save on your favorite spa services"
• Select from your favorite spa services such as NEVRIL, laser treatments, microderms, and more!
• Website: VerdaneSpaDeals.com
• Our logo (attached)
Nice to have
• Modern and creative design. Somehow tying in the "Let your beauty bloom" theme. We don't want the focus to be "The more you buy the more you save"
• We are looking for a unique design that is unlike traditional medical spas in the area that typically include a lot of white and a lot of overly photoshopped images.
• Creativity is key! Something that's different than just text and images. We would be so excited to see that!
Should not have
• Not too much text, but enough to get the point across.

```html
<!DOCTYPE html>
<html lang="en">
<head>
<meta charset="utf-8">
<title>Marigold Jubilee — Verdane Clinical Spa</title>
<link rel="stylesheet" href="https://fonts.googleapis.com/css2?family=Kaushan+Script&family=Sofia&family=Comic+Neue:wght@700&family=Aladin&display=swap">
<style>
  :root {
    --teal-light: #3fe3ec;
    --teal-mid: #22c3cf;
    --teal-dark: #12a0aa;
    --rose: #e8206f;
    --rose-deep: #d4155c;
    --white: #ffffff;
    --ink: #2a2a26;
    --leaf: #cfe9c4;
  }
  html, body {
    margin: 0;
    padding: 0;
    width: 848px;
    height: 1200px;
    overflow: hidden;
  }
  .poster {
    position: relative;
    width: 848px;
    height: 1200px;
    overflow: hidden;
    background: radial-gradient(ellipse 70% 55% at 35% 50%, var(--teal-light) 0%, var(--teal-mid) 55%, var(--teal-dark) 100%);
  }
  .promo-title {
    position: absolute;
    top: 14px;
    left: 0;
    width: 100%;
    margin: 0;
    text-align: center;
    font-family: "Kaushan Script", cursive;
    font-weight: 400;
    font-size: 96px;
    line-height: 130px;
    color: var(--rose);
  }
  .rule {
    position: absolute;
    left: 96px;
    width: 690px;
    height: 3px;
    background: linear-gradient(90deg, rgba(255,255,255,0) 0%, var(--white) 15%, var(--white) 85%, rgba(255,255,255,0) 100%);
  }
  .rule--top { top: 163px; }
  .rule--bottom { top: 253px; }
  .slogan {
    position: absolute;
    top: 170px;
    left: 0;
    width: 100%;
    margin: 0;
    text-align: center;
    font-family: "Sofia", cursive;
    font-size: 60px;
    line-height: 80px;
    color: var(--white);
  }
  .sale-line {
    position: absolute;
    top: 265px;
    left: 0;
    width: 100%;
    margin: 0;
    text-align: center;
    font-family: "Comic Neue", sans-serif;
    font-weight: 700;
    font-size: 34px;
    line-height: 40px;
    color: var(--rose);
    text-shadow: 1px 1px 1px rgba(60, 20, 30, 0.75);
  }
  .bloom {
    position: absolute;
    left: 182px;
    top: 380px;
    width: 508px;
    height: 498px;
  }
  .services {
    position: absolute;
    top: 896px;
    left: 58px;
    width: 764px;
    margin: 0;
    text-align: center;
    font-family: "Aladin", cursive;
    font-size: 46px;
    line-height: 51px;
    letter-spacing: 1px;
    word-spacing: 12px;
    color: var(--rose-deep);
  }
  .services span { display: block; }
  .brand {
    position: absolute;
    right: 32px;
    top: 1090px;
    display: flex;
    align-items: center;
    gap: 12px;
  }
  .brand-dot {
    width: 44px;
    height: 44px;
    border-radius: 50%;
    background: var(--leaf);
  }
  .brand-text {
    display: flex;
    flex-direction: column;
    align-items: flex-end;
  }
  .brand-name {
    font-family: "Aladin", cursive;
    font-size: 46px;
    line-height: 54px;
    color: var(--ink);
    white-space: nowrap;
  }
  .brand-web {
    font-family: "Aladin", cursive;
    font-size: 17px;
    line-height: 22px;
    letter-spacing: 1.5px;
    color: var(--ink);
    white-space: nowrap;
  }
</style>
</head>
<body>
  <div class="poster">
    <h1 class="promo-title">Marigold Jubilee</h1>
    <div class="rule rule--top"></div>
    <p class="slogan">Let Your Beauty Bloom</p>
    <div class="rule rule--bottom"></div>
    <p class="sale-line">The More You Buy, The More You Save</p>

    <svg class="bloom" viewBox="0 0 508 498" role="img" aria-label="Photograph of a single magenta gerbera daisy in full bloom, seen from above, with a yellow-green centre">
      <defs>
        <radialGradient id="bloomFill" cx="50%" cy="50%" r="50%">
          <stop offset="0%" stop-color="#b6bf3a"/>
          <stop offset="12%" stop-color="#c4b83a"/>
          <stop offset="19%" stop-color="#d9903a"/>
          <stop offset="26%" stop-color="#d8245f"/>
          <stop offset="60%" stop-color="#ec2a74"/>
          <stop offset="88%" stop-color="#e41f69"/>
          <stop offset="100%" stop-color="#e41f69" stop-opacity="0"/>
        </radialGradient>
      </defs>
      <ellipse cx="254" cy="249" rx="254" ry="249" fill="url(#bloomFill)"/>
    </svg>

    <p class="services">
      <span>Choose from your favorite spa services</span>
      <span>NEVRIL, Laser Treatments,</span>
      <span>Microderms, and More!</span>
    </p>

    <div class="brand">
      <div class="brand-dot"></div>
      <div class="brand-text">
        <div class="brand-name">Verdane Clinical Spa</div>
        <div class="brand-web">VerdaneSpaDeals.com</div>
      </div>
    </div>
  </div>
</body>
</html>
```